Maple Hollow Bloom Panels Business card

Looking to have a business card design incorporating my logo for my flower wall business.

Industry/Entity Type

Wedding & event planning

Contact Information for Business Card

My business logo, my name - Lena Whitcombe (owner), my tagline - Let us add your final flourish, phone # 401-726-3148, email address - maplehollowbloompanels@mailvane.net, my website - maplehollowbloompanels.net, Instagram handle- @maplehollowbloompanels, FB handle Handle - maplehollowbloompanels

Font styles to use
Other font styles liked:
• Sentaina is the font that is used in my logo

Requirements
Must have
• Would like a double sided business card

```html
<!DOCTYPE html>
<html lang="en">
<head>
<meta charset="utf-8">
<title>Maple Hollow Bloom Panels – Business Card</title>
<link rel="stylesheet" href="https://fonts.googleapis.com/css2?family=Great+Vibes&family=Poppins:wght@400;500&display=swap">
<style>
  :root {
    --canvas: #d9d9d9;
    --card-white: #ffffff;
    --blush: #f9dde8;
    --magenta: #c8177a;
    --gold: #d4ad4c;
    --ink: #1c1c1c;
    --leaf: #3f6b4f;
  }
  * { margin: 0; padding: 0; box-sizing: border-box; }
  html, body { width: 1200px; height: 800px; overflow: hidden; }
  body {
    background: var(--canvas);
    font-family: "Poppins", sans-serif;
    display: flex;
    align-items: center;
    justify-content: center;
    gap: 50px;
  }
  .card {
    position: relative;
    width: 540px;
    height: 309px;
    overflow: hidden;
    box-shadow: 0 14px 30px rgba(0,0,0,0.28);
  }
  .card--front { background: var(--card-white); }
  .card--back { background: var(--blush); }

  .bloom-decoration {
    position: absolute;
    top: -20px;
    right: -30px;
    width: 300px;
    height: 240px;
    border-radius: 50%;
    background: radial-gradient(circle at 55% 45%, rgba(244,196,216,0.45), rgba(244,196,216,0.12) 60%, rgba(244,196,216,0) 75%);
  }
  .card--back .bloom-decoration {
    background: radial-gradient(circle at 55% 45%, rgba(238,176,202,0.45), rgba(238,176,202,0.15) 60%, rgba(238,176,202,0) 75%);
  }

  .band {
    position: absolute;
    left: 0; right: 0; bottom: 0;
    border-top: 3px solid var(--gold);
  }
  .card--front .band { height: 84px; background: var(--blush); }
  .card--back .band { height: 68px; background: var(--card-white); }

  .brand {
    position: absolute;
    display: flex;
    align-items: center;
    gap: 10px;
    color: var(--ink);
    font-weight: 400;
    line-height: 1.25;
  }
  .brand-dot {
    flex: none;
    width: 12px; height: 12px;
    border-radius: 50%;
    background: var(--magenta);
  }
  .card--front .brand { left: 28px; top: 78px; width: 170px; font-size: 17px; }
  .card--back .brand {
    left: 50%; top: 104px;
    transform: translateX(-50%);
    white-space: nowrap;
    font-size: 24px;
  }

  .person { position: absolute; left: 262px; top: 58px; }
  .person-name {
    font-family: "Great Vibes", cursive;
    font-size: 40px;
    color: var(--magenta);
    line-height: 1;
    white-space: nowrap;
  }
  .person-role {
    font-size: 13px;
    color: var(--gold);
    margin-left: 30px;
    margin-top: 2px;
  }

  .contact-list {
    position: absolute;
    left: 180px; top: 150px;
    list-style: none;
    font-size: 12.5px;
    color: var(--magenta);
  }
  .contact-list li { display: flex; align-items: center; gap: 8px; height: 21px; white-space: nowrap; }
  .contact-icon { width: 13px; height: 13px; flex: none; }

  .social-list {
    position: absolute;
    left: 32px; right: 20px; bottom: 30px;
    display: flex;
    justify-content: space-between;
    list-style: none;
    font-size: 13px;
    color: var(--magenta);
  }
  .social-list li { display: flex; align-items: center; gap: 7px; white-space: nowrap; }

  .tagline {
    position: absolute;
    left: 0; right: 0; bottom: 20px;
    text-align: center;
    font-size: 18px;
    letter-spacing: 0.5px;
    color: var(--magenta);
    white-space: nowrap;
  }
</style>
</head>
<body>

  <section class="card card--front" aria-label="Card front">
    <div class="bloom-decoration" role="img" aria-label="Faint outlined peony flower with soft blush dots"></div>
    <div class="band"></div>

    <div class="brand"><span class="brand-dot"></span><span>Maple Hollow Bloom Panels</span></div>

    <div class="person">
      <p class="person-name">Lena Whitcombe</p>
      <p class="person-role">Owner</p>
    </div>

    <ul class="contact-list">
      <li>
        <svg class="contact-icon" viewBox="0 0 16 16"><path fill="var(--leaf)" d="M3.5 1.5l2.5 0 1 3.5-1.8 1.2a9 9 0 0 0 4.6 4.6L11 9l3.5 1v2.5c0 1-1 2-2 2A11 11 0 0 1 1.5 3.5c0-1 1-2 2-2z"/></svg>
        <span>401-726-3148</span>
      </li>
      <li>
        <svg class="contact-icon" viewBox="0 0 16 16"><rect x="1" y="3" width="14" height="10" rx="1" fill="var(--leaf)"/><path d="M1.5 3.8L8 9l6.5-5.2" stroke="#fff" stroke-width="1.2" fill="none"/></svg>
        <span>maplehollowbloompanels@mailvane.net</span>
      </li>
      <li>
        <svg class="contact-icon" viewBox="0 0 16 16"><circle cx="8" cy="8" r="7" fill="var(--leaf)"/><path d="M1 8h14M8 1v14M3 4.5h10M3 11.5h10" stroke="#fff" stroke-width="0.9" fill="none"/><ellipse cx="8" cy="8" rx="3" ry="7" stroke="#fff" stroke-width="0.9" fill="none"/></svg>
        <span>maplehollowbloompanels.net</span>
      </li>
    </ul>

    <ul class="social-list">
      <li><span>@maplehollowbloompanels</span></li>
      <li><span>maplehollowbloompanels</span></li>
    </ul>
  </section>

  <section class="card card--back" aria-label="Card back">
    <div class="bloom-decoration" role="img" aria-label="Faint outlined peony flower with soft blush dots"></div>
    <div class="band"></div>

    <div class="brand"><span class="brand-dot"></span><span>Maple Hollow Bloom Panels</span></div>

    <p class="tagline">Let us add your final flourish</p>
  </section>

</body>
</html>
```